I have an animal hospital. I want a poster to hang in each exam room to show a picture of a normal sized heart and then an enlarged heart of a dog that was fed a grain-free diet. I want to warn people not to feed grain-free diets. Maybe at the top of the poster, "Do you feed grain-free?" and then the x-ray comparison, then the warnings of Canine Dilated Cardiomyopathy.

```html
<!DOCTYPE html>
<html lang="en">
<head>
<meta charset="utf-8">
<title>Do you feed grain-free?</title>
<link href="https://fonts.googleapis.com/css2?family=Montserrat:wght@500;600;700;800&display=swap" rel="stylesheet">
<style>
  :root {
    --navy: #0f2a6b;
    --navy-deep: #0a2260;
    --red: #c8161c;
    --red-deep: #a51218;
    --white: #ffffff;
    --ink-blue: #142f6e;
    --panel-dark: #000000;
    --panel-grey: #555555;
    --ring: #d01c20;
    --silver-light: #e6e6e6;
    --silver-dark: #8a8a8a;
  }
  * { margin: 0; padding: 0; box-sizing: border-box; }
  html, body { width: 900px; height: 1200px; overflow: hidden; background: var(--white); }
  .poster {
    position: relative;
    width: 900px;
    height: 1200px;
    overflow: hidden;
    font-family: "Montserrat", sans-serif;
    color: var(--white);
    font-variant: small-caps;
  }
  .header {
    position: absolute; left: 0; top: 0; width: 900px; height: 188px;
    background: var(--navy);
    text-align: center;
  }
  .header__lead {
    position: absolute; top: 18px; width: 100%;
    font-size: 58px; font-weight: 700; line-height: 1;
    text-shadow: 0 2px 3px rgba(0,0,0,.35);
  }
  .header__title {
    position: absolute; top: 74px; width: 100%;
    font-size: 100px; font-weight: 800; line-height: 1;
    font-variant: normal; letter-spacing: -1px;
    text-shadow: 0 3px 4px rgba(0,0,0,.35);
  }
  .divider {
    position: absolute; left: 0; width: 900px; height: 14px;
    background: linear-gradient(to bottom, var(--silver-dark), var(--silver-light) 45%, var(--silver-dark));
  }
  .divider--top { top: 188px; }
  .divider--bottom { top: 1038px; }
  .comparison {
    position: absolute; left: 0; top: 380px; width: 900px; height: 658px;
  }
  .xray {
    position: absolute; top: 0; height: 658px;
  }
  .xray--grain-free {
    left: 0; width: 450px;
    background: radial-gradient(ellipse 170px 320px at 225px 390px, #9a9a9a, #4a4a4a 55%, var(--panel-dark) 85%);
  }
  .xray--grain {
    left: 450px; width: 450px;
    background: radial-gradient(ellipse 170px 260px at 243px 380px, #b4b4b4, #7a7a7a 55%, var(--panel-grey) 85%);
  }
  .xray__caption {
    position: absolute; width: 100%; text-align: center;
    font-size: 27px; font-weight: 500; line-height: 1;
    text-shadow: 0 0 6px #000;
  }
  .xray--grain-free .xray__caption { top: 568px; }
  .xray--grain .xray__caption { top: 516px; left: 0; }
  .rings { position: absolute; left: 0; top: 0; }
  .banner { position: absolute; left: 0; top: 200px; }
  .banner__heading {
    position: absolute; top: 208px; width: 100%; text-align: center;
    font-size: 40px; font-weight: 700; line-height: 1;
    text-shadow: 0 2px 3px rgba(0,0,0,.35);
  }
  .diet-label {
    position: absolute; color: var(--ink-blue);
    font-size: 38px; font-weight: 600; line-height: 1;
  }
  .diet-label--grain-free { left: 62px; top: 346px; transform: rotate(3deg); }
  .diet-label--grain { left: 584px; top: 342px; transform: rotate(1.5deg); }
  .footer {
    position: absolute; left: 0; top: 1052px; width: 900px; height: 148px;
    background: var(--navy-deep); text-align: center;
  }
  .footer__warning {
    position: absolute; top: 24px; width: 100%;
    font-size: 37px; font-weight: 700; line-height: 1;
  }
  .footer__condition {
    position: absolute; top: 68px; width: 100%;
    font-size: 51px; font-weight: 700; line-height: 1;
  }
</style>
</head>
<body>
<main class="poster">
  <header class="header">
    <p class="header__lead">Do you feed</p>
    <h1 class="header__title">GRAIN-FREE?</h1>
  </header>
  <div class="divider divider--top"></div>

  <section class="comparison">
    <div class="xray xray--grain-free" role="img" aria-label="Chest x-ray of a dog fed a grain-free diet showing an enlarged heart">
      <p class="xray__caption">Larger heart size</p>
    </div>
    <div class="xray xray--grain" role="img" aria-label="Chest x-ray of a dog fed a grain diet showing a normal sized heart">
      <p class="xray__caption">Normal heart size</p>
    </div>
    <svg class="rings" width="900" height="658" viewBox="0 0 900 658" aria-hidden="true">
      <circle cx="220" cy="428" r="126" fill="none" stroke="var(--ring)" stroke-width="6"/>
      <circle cx="693" cy="389" r="110" fill="none" stroke="var(--ring)" stroke-width="6"/>
    </svg>
  </section>

  <svg class="banner" width="900" height="240" viewBox="0 200 900 240" aria-hidden="true">
    <defs>
      <linearGradient id="redBand" x1="0" y1="0" x2="0" y2="1">
        <stop offset="0" stop-color="var(--red-deep)"/>
        <stop offset="1" stop-color="var(--red)"/>
      </linearGradient>
    </defs>
    <path d="M0 200 H900 V317 Q650 300 530 330 L370 330 Q200 300 0 339 Z" fill="url(#redBand)"/>
    <path d="M0 339 Q200 300 370 330 L530 330 Q650 300 900 317 V393 Q640 395 450 434 Q260 395 0 418 Z" fill="var(--white)"/>
    <path d="M450 412 C420 380 368 350 368 302 C368 274 390 262 410 262 C430 262 444 274 450 288 C456 274 470 262 490 262 C510 262 532 274 532 302 C532 350 480 380 450 412 Z" fill="var(--white)" stroke="var(--red)" stroke-width="9" stroke-linejoin="round"/>
  </svg>
  <h2 class="banner__heading">Size comparision of a Dog’s heart</h2>
  <p class="diet-label diet-label--grain-free">Grain-Free Diet</p>
  <p class="diet-label diet-label--grain">Grain Diet</p>

  <div class="divider divider--bottom"></div>
  <footer class="footer">
    <p class="footer__warning">Avoid Feeding grain-free diets to prevent</p>
    <p class="footer__condition">Canine Dilated Cardiomyopathy</p>
  </footer>
</main>
</body>
</html>
```